Amber Tides: Lantern Tales from Seven Winters by the Northern Sea and Other Small Wonders

Good day! I am excited to work again with you, amazing designers! This time I am looking for the cover design of my book.
Dimensions 6” x 9”
The book name is as my name project. I love simplicity, but yet that is impactful. I love colours, I don't have a specific colour in mind, but I like the mustard colour as the one in the logo of my company. I am open to ideas! I have attached some cover samples that I like so that it gives a better idea of what I have on mind.
I am looking for something that looks professional, yet, not super serious, that it's approachable to people. Something that calls their attention at first glance.
I am working with my editor and my interior designer as well to finalize this part of the book. I will be working with the person that I select for the book design to finalize it.
About the book, here a passage of an unedited version of the introduction for guidance :
My intention is to take you on a journey to help you to understand what is going on in your mind so that you get out from anything that is holding you back in your life. My intention is to guide you to start fully living and experiencing a life that your mind even have yet conceived. To experience a life where you live fearless and without suffering. Living your life where you are the navigator and the creator of how you are experiencing it and you are living in a world of possibilities where there are no limitations.
For it, we will start to understand more about the mind and about the brain. I am not a neuroscientist and neither I consider my self an expert in the workings of the brain, what I know is the result of my fascination about our brain. This curiosity and the part of me that likes to understand how things work took me to read, research and learn about how our brain works and how its intrinsic mechanisms are subconsciously influencing and limiting us. I encourage you to stay on this part, it can be a bit technical, but understanding how it works will empower you not to allow your mind to dictate the way you approach your life and to live on autopilot.
We will continue to describe how you have been programmed throughout your life, putting you inside a box limited by your subconscious beliefs and ideas about the world. In this part, we will also discuss what ego is, how it is subconsciously limiting you and how the ways of when ego manifests itself are limiting you and making you suffer. Now that you know how you have been enclosed in your mind for all your life, we will move to discuss how you can get out of it. You will learn how to master your emotions to eliminate your suffering and not allow them to control the direction of your life and use them as a mechanism to get out from your programed mind. We continue to discuss how to leverage the power of your mind and harness your power of choice. Finally, I invite you to see yourself as a holistic being so that you start truly living and take control over the direction of your life, by nourishing and taking care of all those aspects of you utilizing their wisdom and synergy to achieve higher connection within yourself, your soul and live your life in a higher level of consciousness with peace, flow, love and purpose.

```html
<!DOCTYPE html>
<html lang="en">
<head>
<meta charset="UTF-8">
<title>Amber Tides — Book Cover</title>
<link rel="stylesheet" href="https://fonts.googleapis.com/css2?family=Oswald:wght@700&family=Poppins:wght@400;600&display=swap">
<style>
  :root {
    --stage: #eeeff0;
    --cover-deep: #1c3f78;
    --cover-mid: #2563a8;
    --cover-light: #2d6fb6;
    --title-white: #ffffff;
    --art-top: #dfe3ea;
    --art-bottom: #7f8fa8;
  }
  * { margin: 0; padding: 0; box-sizing: border-box; }
  html, body {
    width: 1200px;
    height: 1108px;
    overflow: hidden;
    background: radial-gradient(ellipse at center, #ffffff 0%, var(--stage) 75%);
  }
  .cover {
    position: absolute;
    left: 270px;
    top: 59px;
    width: 660px;
    height: 990px;
    overflow: hidden;
    background: radial-gradient(ellipse 70% 55% at 50% 42%, var(--cover-light) 0%, var(--cover-mid) 40%, var(--cover-deep) 100%);
    box-shadow: 0 18px 40px rgba(0, 0, 0, 0.18);
  }
  .title {
    position: absolute;
    left: 0;
    right: 0;
    top: 40px;
    text-align: center;
    font-family: "Oswald", sans-serif;
    font-weight: 700;
    color: var(--title-white);
    text-transform: uppercase;
    line-height: 0.9;
  }
  .title-top {
    display: block;
    font-size: 190px;
    letter-spacing: -4px;
  }
  .title-main {
    display: block;
    font-size: 240px;
    letter-spacing: -6px;
    margin-top: 6px;
  }
  .cover-art {
    position: absolute;
    left: 420px;
    top: 585px;
    width: 240px;
    height: 405px;
    background: linear-gradient(180deg, var(--art-top) 0%, var(--art-bottom) 100%);
    opacity: 0.35;
  }
  .subtitle {
    position: absolute;
    left: 60px;
    top: 700px;
    width: 350px;
    text-align: center;
    font-family: "Poppins", sans-serif;
    font-weight: 400;
    font-size: 24px;
    line-height: 1.3;
    color: var(--title-white);
  }
  .author {
    position: absolute;
    left: 0;
    width: 520px;
    top: 905px;
    text-align: center;
    font-family: "Poppins", sans-serif;
    font-weight: 600;
    font-size: 30px;
    letter-spacing: 2px;
    color: var(--title-white);
    text-transform: uppercase;
  }
</style>
</head>
<body>
  <main class="cover">
    <div class="cover-art" role="img" aria-label="Photograph: a hand in a suit sleeve holding up a white paper plane with a small flame trail beneath the title"></div>

    <h1 class="title">
      <span class="title-top">Amber</span>
      <span class="title-main">Tides</span>
    </h1>

    <p class="subtitle">Lantern Tales from Seven Winters by the Northern Sea and Other Small Wonders</p>

    <p class="author">Rowan Vale</p>
  </main>
</body>
</html>
```